Design and Renovation Company Luxury Business Card

I want to create a luxury business card for a Design and Renovation Firm . We will use our current logo. The company name is 742BUILD. We do not want anything standard. We need a very unique concept.
Please see uploaded inspiration. I really like the textured paper option. I would like the card to be thick with debossing, and/or embossing options. The logo has orange in it but I would like to see the card with and without the orange. I think the orange may make the company feel less high-end. The goal is to elevate the logo not match its vibe per se of the logo. We want something very unique, not standard at all!
I would like a space for :
Logo,
Name,
Position,
Email,
Office number,
Website Address,
Business Address,
Thank you!
Have fun!
Target Market(s)
Home owners Age 35 +
Industry/Entity Type
Design and Renovation
Contact Information for Business Card
Logo, Name, Position, Email, Office number, Website Address, Business Address,.
Colors
Designer to choose colors to be used in the design.
Requirements
Must have
- A luxury designer feel. Must be black or dark grey but open to other luxury ideas.
Nice to have
- Gold, silver, black embossing or debossing. Textured paper design.
Should not have
- A cheap look and feel.

```html
<!DOCTYPE html>
<html lang="en">
<head>
<meta charset="utf-8">
<title>742BUILD Business Card</title>
<link href="https://fonts.googleapis.com/css2?family=Titillium+Web:wght@400&family=Arimo:wght@400;700&display=swap" rel="stylesheet">
<style>
  :root {
    --bg: #1f1f1f;
    --card: #2b2b2b;
    --card-edge: #363636;
    --silver: #c9c9c9;
    --white: #f2f2f2;
    --orange: #f4931e;
    --panel-light: #6a6a6a;
    --panel-dark: #3a3a3a;
  }
  * { margin: 0; padding: 0; box-sizing: border-box; }
  html, body { width: 1200px; height: 689px; overflow: hidden; background: var(--bg); }
  .stage {
    position: relative; width: 1200px; height: 689px;
    display: flex; align-items: center; justify-content: center; gap: 60px;
  }
  .card {
    position: relative; width: 520px; height: 298px;
    background: var(--card); border-radius: 18px;
    border: 1px solid var(--card-edge);
    box-shadow: 0 18px 40px rgba(0,0,0,.5);
    overflow: hidden;
  }
  /* front */
  .card--front { display: flex; align-items: center; justify-content: center; }
  .front-name {
    font-family: "Titillium Web", sans-serif; font-weight: 400;
    font-size: 64px; line-height: 1; letter-spacing: 2px; color: var(--silver);
  }
  /* back */
  .details { position: absolute; left: 34px; top: 36px; width: 280px; }
  .brand-name {
    font-family: "Titillium Web", sans-serif; font-weight: 400; font-size: 40px; line-height: 1;
    letter-spacing: 1.5px; color: var(--white);
  }
  .person { margin-top: 22px; font-family: "Arimo", sans-serif; }
  .person__name { font-weight: 700; font-size: 19px; line-height: 1.2; color: var(--orange); letter-spacing: .5px; }
  .person__role { font-size: 12.5px; color: var(--white); margin-top: 2px; }
  .address {
    margin-top: 18px; font-family: "Arimo", sans-serif; font-style: normal;
    font-size: 12.5px; line-height: 1.4; color: var(--white);
  }
  .contact { list-style: none; margin-top: 16px; font-family: "Arimo", sans-serif; font-size: 12.5px; color: var(--white); }
  .contact li { display: flex; align-items: center; gap: 8px; line-height: 1.45; }
  .contact svg { width: 11px; height: 11px; fill: var(--orange); flex: none; }
  .panel {
    position: absolute; right: 34px; top: 40px; width: 190px; height: 218px;
    border-radius: 4px;
    background: linear-gradient(160deg, var(--panel-light), var(--panel-dark));
  }
</style>
</head>
<body>
<main class="stage">
  <section class="card card--front" aria-label="Card front">
    <span class="front-name">742BUILD</span>
  </section>

  <section class="card card--back" aria-label="Card back">
    <div class="details">
      <div class="brand-name">742BUILD</div>
      <div class="person">
        <div class="person__name">DANIEL MORROW</div>
        <div class="person__role">President</div>
      </div>
      <address class="address">
        1420 Alder Court<br>Halden, Canada 20815
      </address>
      <ul class="contact">
        <li><svg viewBox="0 0 24 24"><path d="M6.6 10.8a15.1 15.1 0 0 0 6.6 6.6l2.2-2.2a1 1 0 0 1 1-.25 11.4 11.4 0 0 0 3.6.57 1 1 0 0 1 1 1V20a1 1 0 0 1-1 1A17 17 0 0 1 3 4a1 1 0 0 1 1-1h3.5a1 1 0 0 1 1 1c0 1.25.2 2.45.57 3.57a1 1 0 0 1-.25 1z"/></svg>555-218-4096</li>
        <li><svg viewBox="0 0 24 24"><path d="M7 1h10a2 2 0 0 1 2 2v18a2 2 0 0 1-2 2H7a2 2 0 0 1-2-2V3a2 2 0 0 1 2-2zm0 3v15h10V4z"/></svg>info@742build.com</li>
        <li><svg viewBox="0 0 24 24"><path d="M2 4h20v16H2zm2 2v.5l8 5 8-5V6zm0 3v9h16V9l-8 5z"/></svg>www.742build.com</li>
      </ul>
    </div>
    <div class="panel" role="img" aria-label="Decorative grey gradient panel"></div>
  </section>
</main>
</body>
</html>
```